Webpage Toggle Button Graphics

We are a webhosting company that sells Hosted Servers (Windows/Linux etc). We have for each service in our catalogue a number of on/off/maybe toggle buttons (not actally buttons, but display). Out current design is not modern enough, and would like a new design for the concept. (current screenshot is attached).
Updates

It seems I need to clarify something.  The ICONS I need are for the Buttons in the attachment marked Anti-virus, File Backup, HIDS, DR.  Not anything else on the page. The New icons do need to fit in with the look and feel of the page, and ideally are smaller (so we can fit more of these ICONS on the page). Thanks              

Industry/Entity Type

It Company

Requirements
Must have
• Generic Button Display, with 4 states- ON (Red/Bad, I have this feature), OFF (Green/Good, I do not have this feature), N/A (greyed out, feature is not available), MAYBE (Blue, I dont have this feature but its not really Red/Bad)
• Prefer a generic version with a single visual cue (dot/button or whatever) and a Text Description (i.e. not a custom ICON for each feature)
• Needs to fit in the space similiar to the screenshot, but Ideally smaller.
• Initial buttons are to be for:
• Anti-Virus (AV)
• Backup (Back)
• Host Intrusion Detection (HIDS)
• Disaster Recovery (DR)
• DDOS (DDOS)
• Can submittions be in the format of the attachment with your designs embedded into the picture to show what it will look like in production. May Icon 1-RED, 2, Green, 3 Blue, 4 - Greyed out.
Nice to have
• Ideally the button/display is generic, and our developers can just add the text for any future buttons

```html
<!DOCTYPE html>
<html lang="en">
<head>
<meta charset="utf-8">
<title>Service Feature Status</title>
<link rel="stylesheet" href="https://fonts.googleapis.com/css2?family=Arimo:wght@400;700&display=swap">
<style>
  :root {
    --page-bg: #ffffff;
    --band-bg: #eef2f6;
    --rule-grey: #dde3ea;
    --rule-blue: #cfe3f2;
    --heading: #555a60;
    --label: #2f3a45;
    --chip-bg: #ffffff;
    --chip-border: #c9d3dd;
    --state-on: #e0352b;
    --state-on-soft: #fbe1df;
    --state-off: #3aa935;
    --state-off-soft: #e0f3df;
    --state-maybe: #1a9ad6;
    --state-maybe-soft: #dcf0fa;
    --state-na: #9aa3ab;
    --state-na-soft: #eceff2;
    --label-na: #8e979f;
    --sort-blue: #2f7fc8;
    --action-border: #b9d4ec;
  }
  * { box-sizing: border-box; margin: 0; padding: 0; }
  html, body { width: 1200px; height: 900px; overflow: hidden; background: var(--page-bg); }
  body { position: relative; font-family: "Arimo", Arial, sans-serif; }

  .table-rule-left { position: absolute; left: 68px; top: 110px; width: 1px; height: 638px; background: var(--rule-grey); }
  .table-rule-actions { position: absolute; left: 945px; top: 218px; width: 1px; height: 530px; background: var(--rule-blue); }

  .col-heading { position: absolute; font-weight: 700; font-size: 26px; color: var(--heading); line-height: 1; display: flex; align-items: center; gap: 4px; }
  .col-heading--settings { left: 76px; top: 178px; }
  .col-heading--features { left: 292px; top: 128px; flex-direction: column; align-items: flex-start; gap: 24px; }
  .col-heading--features .heading-line { display: flex; align-items: center; gap: 4px; }
  .col-heading--associated { left: 710px; top: 178px; }

  .sort-toggle { width: 30px; height: 30px; border-radius: 50%; border: 2px solid var(--rule-blue); background: #fff; display: inline-flex; align-items: center; justify-content: center; }

  .service-row { position: absolute; left: 69px; width: 1131px; }
  .service-row--band { background: var(--band-bg); }
  .row-1 { top: 218px; height: 150px; --mid: 66px; }
  .row-2 { top: 368px; height: 130px; --mid: 68px; }
  .row-3 { top: 498px; height: 128px; --mid: 73px; }
  .row-4 { top: 626px; height: 122px; --mid: 78px; }

  .feature-list { position: absolute; left: 10px; top: var(--mid); transform: translateY(-50%); display: flex; gap: 8px; list-style: none; }
  .feature-status {
    display: inline-flex; align-items: center; gap: 8px; height: 32px; padding: 0 14px 0 10px;
    border-radius: 16px; background: var(--chip-bg); border: 1px solid var(--chip-border);
    font-size: 16px; color: var(--label); white-space: nowrap;
    box-shadow: 0 1px 2px rgba(30, 50, 70, 0.08);
  }
  .feature-status__dot { width: 12px; height: 12px; border-radius: 50%; flex: none; }
  .feature-status--on .feature-status__dot { background: var(--state-on); box-shadow: 0 0 0 4px var(--state-on-soft); }
  .feature-status--off .feature-status__dot { background: var(--state-off); box-shadow: 0 0 0 4px var(--state-off-soft); }
  .feature-status--maybe .feature-status__dot { background: var(--state-maybe); box-shadow: 0 0 0 4px var(--state-maybe-soft); }
  .feature-status--na { color: var(--label-na); background: #f6f8fa; border-style: dashed; box-shadow: none; }
  .feature-status--na .feature-status__dot { background: var(--state-na); box-shadow: 0 0 0 4px var(--state-na-soft); }

  .actions-menu { position: absolute; left: 881px; top: var(--mid); transform: translateY(-50%); width: 225px; height: 60px; background: #fff; border: 2px solid var(--action-border); border-radius: 4px; display: flex; align-items: center; justify-content: space-between; padding: 0 14px 0 22px; }
  .actions-menu__text { font-size: 28px; color: var(--heading); }
  .actions-menu__button { width: 40px; height: 30px; border: 1px solid #7a7a7a; background: linear-gradient(180deg, #fafafa, #dcdcdc); display: flex; align-items: center; justify-content: center; }
</style>
</head>
<body>
  <div class="table-rule-left"></div>

  <div class="col-heading col-heading--settings">Settings
    <span class="sort-toggle"><svg width="12" height="8" viewBox="0 0 12 8"><path d="M0 0h12L6 8z" fill="var(--sort-blue)"/></svg></span>
  </div>
  <div class="col-heading col-heading--features">
    <span class="heading-line">Associated</span>
    <span class="heading-line">Features
      <span class="sort-toggle"><svg width="12" height="8" viewBox="0 0 12 8"><path d="M0 0h12L6 8z" fill="var(--sort-blue)"/></svg></span>
    </span>
  </div>
  <div class="col-heading col-heading--associated">Associated Features</div>

  <div class="service-row service-row--band row-1">
    <ul class="feature-list">
      <li class="feature-status feature-status--on"><span class="feature-status__dot"></span>Anti Virus</li>
      <li class="feature-status feature-status--off"><span class="feature-status__dot"></span>File Backup</li>
      <li class="feature-status feature-status--maybe"><span class="feature-status__dot"></span>HIDS</li>
      <li class="feature-status feature-status--na"><span class="feature-status__dot"></span>DR</li>
      <li class="feature-status feature-status--off"><span class="feature-status__dot"></span>DDOS</li>
    </ul>
    <div class="actions-menu"><span class="actions-menu__text">Actions</span><span class="actions-menu__button"><svg width="12" height="7" viewBox="0 0 12 7"><path d="M0 0h12L6 7z" fill="#111"/></svg></span></div>
  </div>

  <div class="service-row row-2">
    <ul class="feature-list">
      <li class="feature-status feature-status--on"><span class="feature-status__dot"></span>Anti Virus</li>
      <li class="feature-status feature-status--off"><span class="feature-status__dot"></span>File Backup</li>
      <li class="feature-status feature-status--maybe"><span class="feature-status__dot"></span>HIDS</li>
      <li class="feature-status feature-status--na"><span class="feature-status__dot"></span>DR</li>
      <li class="feature-status feature-status--off"><span class="feature-status__dot"></span>DDOS</li>
    </ul>
    <div class="actions-menu"><span class="actions-menu__text">Actions</span><span class="actions-menu__button"><svg width="12" height="7" viewBox="0 0 12 7"><path d="M0 0h12L6 7z" fill="#111"/></svg></span></div>
  </div>

  <div class="service-row service-row--band row-3">
    <ul class="feature-list">
      <li class="feature-status feature-status--on"><span class="feature-status__dot"></span>Anti Virus</li>
      <li class="feature-status feature-status--off"><span class="feature-status__dot"></span>File Backup</li>
      <li class="feature-status feature-status--maybe"><span class="feature-status__dot"></span>HIDS</li>
      <li class="feature-status feature-status--na"><span class="feature-status__dot"></span>DR</li>
      <li class="feature-status feature-status--off"><span class="feature-status__dot"></span>DDOS</li>
    </ul>
    <div class="actions-menu"><span class="actions-menu__text">Actions</span><span class="actions-menu__button"><svg width="12" height="7" viewBox="0 0 12 7"><path d="M0 0h12L6 7z" fill="#111"/></svg></span></div>
  </div>

  <div class="service-row row-4">
    <ul class="feature-list">
      <li class="feature-status feature-status--on"><span class="feature-status__dot"></span>Anti Virus</li>
      <li class="feature-status feature-status--off"><span class="feature-status__dot"></span>File Backup</li>
      <li class="feature-status feature-status--maybe"><span class="feature-status__dot"></span>HIDS</li>
      <li class="feature-status feature-status--na"><span class="feature-status__dot"></span>DR</li>
      <li class="feature-status feature-status--off"><span class="feature-status__dot"></span>DDOS</li>
    </ul>
    <div class="actions-menu"><span class="actions-menu__text">Actions</span><span class="actions-menu__button"><svg width="12" height="7" viewBox="0 0 12 7"><path d="M0 0h12L6 7z" fill="#111"/></svg></span></div>
  </div>

  <div class="table-rule-actions"></div>
</body>
</html>
```